Simple templates for management consulting firm

Vireo Associates is a management consulting firm based in the DC area. We have all the basic templates but would like to tweak them so they look consistent.

Check us out at www.vireoassociates-example.com

For this project we would like to get
a tweaked powerpoint template (header should be up)
a letter template for letters
a fax template

Current templates and our logo are attached.
Updates

We just increased the budget of this project.

We got questions about the project. Here are our thoughts on this one:

Please include the logo into the fax template. If you find improvements in the layout then feel free to make those. Let's not overthink this too much. Keep it simple :)

We like The powerpoint concept as is. The slide titles are for some reasons on the bottom. It seems to irritate some folks. If you can switch the slide titles to the top, keep the look and feel of the slides and work in the logo then that would be fantastic.

The letter head should include the following

Vireo Associates, LLC Box 5827, Millbrook, VA 20147 Phone 703 518-9461, Fax 703 286 7135, www.vireoassociates-example.com and the logo.

Again, let's keep it simple.

Thank you for considering this project.

We just realize that we are not necessarily inisting to use the red in the slides.
Any approach that would work with the logo will be considered.

Thanks for your creativity.

Target Market(s)

tech companies, Pinnacle 400, venture capitalists

Industry/Entity Type

Management Consulting

Requirements
Must have
• Keep it simple please

```html
<!DOCTYPE html>
<html lang="en">
<head>
<meta charset="utf-8">
<title>Vireo Associates – Fax and Letterhead</title>
<link rel="stylesheet" href="https://fonts.googleapis.com/css2?family=Gelasio:wght@400;700&family=Open+Sans:wght@700&display=swap">
<style>
  :root {
    --backdrop: #d4d4d4;
    --paper: #ffffff;
    --ink: #222222;
    --ink-soft: #3a3a3a;
    --rule: #7a7a7a;
    --brand-grey: #8a8a8a;
    --brand-gold: #d8aa2e;
    --footer-grey: #6b6b6b;
  }
  * { box-sizing: border-box; margin: 0; padding: 0; }
  html, body {
    width: 1200px; height: 743px; overflow: hidden;
    background: var(--backdrop);
  }
  .canvas { position: relative; width: 1200px; height: 743px; }
  .sheet {
    position: absolute; top: 28px; width: 528px; height: 684px;
    background: var(--paper);
    box-shadow: 0 0 6px rgba(0,0,0,0.25);
    font-family: "Gelasio", Georgia, serif;
    color: var(--ink);
  }
  .sheet--fax { left: 38px; }
  .sheet--letter { left: 634px; }

  .brand { position: absolute; left: 27px; top: 40px; display: flex; align-items: center; gap: 8px; }
  .brand__dot { width: 40px; height: 40px; border-radius: 50%; background: var(--brand-gold); }
  .brand__name {
    font-family: "Gelasio", Georgia, serif; font-weight: 400;
    font-size: 21px; line-height: 1.05; color: var(--brand-grey);
  }

  .sender { position: absolute; left: 227px; top: 33px; font-size: 9.5px; line-height: 11.5px; color: var(--ink-soft); }
  .sender__date { margin-top: 10px; }

  .doc-title {
    position: absolute; right: 33px; top: 22px;
    font-size: 78px; line-height: 1; font-weight: 400; color: var(--ink-soft);
  }

  .rule { position: absolute; left: 32px; width: 463px; height: 0; border-top: 1px solid var(--rule); }
  .rule--top { top: 124px; }
  .rule--bottom { top: 579px; }

  .routing { position: absolute; left: 23px; top: 156px; width: 474px; }
  .routing__row {
    display: flex; height: 21.2px; align-items: flex-end;
    border-bottom: 1px dashed var(--ink); padding-bottom: 1px;
    font-size: 10.5px; white-space: nowrap;
  }
  .routing__cell { padding-left: 5px; }
  .routing__cell--to { width: 257px; }
  .routing__row--head { font-size: 11.5px; }
  .routing__label { font-weight: 700; }

  .flags { position: absolute; left: 32px; top: 597px; list-style: none; }
  .flags__item {
    display: flex; align-items: center; gap: 9px; height: 20.8px;
    font-size: 8px; font-weight: 700;
  }
  .flags__box { width: 11px; height: 11px; border: 1px solid var(--ink); }

  .letter-footer {
    position: absolute; left: 0; right: 0; top: 656px; text-align: center;
    font-family: "Open Sans", Arial, sans-serif; font-weight: 700;
    font-size: 8px; color: var(--footer-grey);
  }
  .letter-footer__web { color: var(--brand-gold); }
</style>
</head>
<body>
<main class="canvas">

  <section class="sheet sheet--fax" aria-label="Fax cover template">
    <div class="brand">
      <span class="brand__dot"></span>
      <span class="brand__name">Vireo<br>Associates</span>
    </div>

    <address class="sender" style="font-style:normal">
      VIREO ASSOCIATES, LLC<br>
      www.vireoassociates-example.com<br>
      P 703 724 3058<br>
      F 703 286 7135
      <div class="sender__date">[Pick the date]</div>
    </address>

    <h1 class="doc-title">Fax</h1>

    <div class="rule rule--top"></div>

    <div class="routing">
      <div class="routing__row routing__row--head">
        <div class="routing__cell routing__cell--to"><span class="routing__label">TO:</span> «GreetingLine»</div>
        <div class="routing__cell"><span class="routing__label">FROM: Martin Keller</span></div>
      </div>
      <div class="routing__row">
        <div class="routing__cell routing__cell--to">[TYPE THE RECIPIENT COMPANY NAME]</div>
        <div class="routing__cell">PAGES:&nbsp; [Type the number of pages]</div>
      </div>
      <div class="routing__row">
        <div class="routing__cell routing__cell--to">FAX: «Business Fax»</div>
        <div class="routing__cell">FAX:&nbsp; [Type the sender fax number]</div>
      </div>
      <div class="routing__row">
        <div class="routing__cell routing__cell--to">PHONE:&nbsp; «Business Phone»</div>
        <div class="routing__cell">PHONE:&nbsp; [Type the sender phone number]</div>
      </div>
      <div class="routing__row"></div>
      <div class="routing__row"></div>
      <div class="routing__row"></div>
    </div>

    <div class="rule rule--bottom"></div>

    <ul class="flags">
      <li class="flags__item"><span class="flags__box"></span>Urgent</li>
      <li class="flags__item"><span class="flags__box"></span>Please review</li>
      <li class="flags__item"><span class="flags__box"></span>Please comment</li>
      <li class="flags__item"><span class="flags__box"></span>For your records</li>
    </ul>
  </section>

  <section class="sheet sheet--letter" aria-label="Letterhead template">
    <div class="brand">
      <span class="brand__dot"></span>
      <span class="brand__name">Vireo<br>Associates</span>
    </div>

    <p class="letter-footer">
      Vireo Associates, LLC Box 5827, Millbrook, VA 20147 • Phone 703 518-9461 • Fax 703 286 7135 •
      <span class="letter-footer__web">www.vireoassociates-example.com</span>
    </p>
  </section>

</main>
</body>
</html>
```